Copper Ridge Business Cards For New Startup

I am looking for you to design some business cards for a new startup https://copperridgehub.example. I have supplied logo, brand guidelines and our signatures as a guide.

We need this to reflect the brand guidelines and the website for brand consistency,

What is Copper Ridge?

Mallorca's Business Growth Community
Join your new business community full of passionate entrepreneurs who
love to solve problems and help each other grow together!

Any questions you can ask.

Target Market(s)

Business to Business

Contact Information for Business Card

These are attached (signatures) to the job

Font styles to use
Other font styles liked:
• Open Sans

Requirements
Must have
• Match design guidelines
Nice to have
• Photos of our faces so people remember us

```html
<!DOCTYPE html>
<html lang="en">
<head>
<meta charset="utf-8">
<title>Copper Ridge Business Cards</title>
<link href="https://fonts.googleapis.com/css2?family=Open+Sans:wght@400;600;700&display=swap" rel="stylesheet">
<style>
  :root {
    --stage-green: #818436;
    --stage-copper: #9a6a2c;
    --card-green: #676a2e;
    --card-brown: #674f22;
    --sliver-green: #6e712f;
    --sliver-brown: #5f4a20;
    --ink: #ffffff;
    --shadow: rgba(30, 24, 8, 0.45);
  }
  * { margin: 0; padding: 0; box-sizing: border-box; }
  html, body { width: 960px; height: 1200px; overflow: hidden; }
  body { font-family: "Open Sans", sans-serif; color: var(--ink); }
  .stage { position: relative; width: 960px; height: 1200px; background: var(--stage-green); overflow: hidden; }
  .stage-split { position: absolute; inset: 0; }
  .card {
    position: absolute; left: 69px; width: 823px; height: 458px; overflow: hidden;
    box-shadow: 0 14px 28px var(--shadow);
  }
  .card-front { top: 76px; background: var(--card-green); }
  .card-back { top: 636px; background: var(--card-brown); }
  .card-shapes { position: absolute; inset: 0; width: 100%; height: 100%; }
  .portrait {
    position: absolute; left: 66px; top: 34px; width: 158px; height: 142px;
    background: linear-gradient(180deg, #7a7152 0%, #8c7a66 55%, #34405a 100%);
  }
  .person-name {
    position: absolute; left: 0; width: 288px; top: 176px; text-align: center;
    font-size: 32px; font-weight: 700; line-height: 1; letter-spacing: -0.3px;
  }
  .person-role {
    position: absolute; left: 0; width: 288px; top: 212px; text-align: center;
    font-size: 15px; font-weight: 400; line-height: 1;
  }
  .contact-pill {
    position: absolute; display: flex; align-items: center; gap: 10px;
    font-size: 16px; font-weight: 700; letter-spacing: 2px; white-space: nowrap;
    box-shadow: 0 6px 8px var(--shadow);
  }
  .contact-pill svg { flex: none; }
  .pill-email { left: 0; top: 262px; width: 258px; height: 45px; padding-left: 9px; gap: 8px;
    background: var(--card-green); border-radius: 0 22px 22px 0; font-size: 13px; letter-spacing: 1.2px; }
  .pill-phone { left: 0; top: 350px; width: 258px; height: 42px; padding-left: 12px;
    background: var(--card-green); border-radius: 0 21px 21px 0; }
  .pill-web { left: 566px; top: 50px; width: 258px; height: 44px; padding-left: 24px; gap: 8px;
    background: var(--card-brown); border-radius: 22px 0 0 22px; font-size: 13px; letter-spacing: 1.2px; }
  .brand-tile { position: absolute; background: var(--card-green); border-radius: 4px; }
  .brand-name { position: absolute; text-align: center; font-weight: 600; line-height: 1; white-space: nowrap; letter-spacing: 0.5px; }
  .card-front .brand-tile { left: 618px; top: 223px; width: 105px; height: 105px; }
  .card-front .brand-name { left: 531px; width: 280px; top: 344px; font-size: 28px; }
  .card-back .brand-tile { left: 360px; top: 30px; width: 93px; height: 93px; }
  .card-back .brand-name { left: 276px; width: 260px; top: 135px; font-size: 26px; }
</style>
</head>
<body>
<main class="stage">
  <svg class="stage-split" width="960" height="1200" viewBox="0 0 960 1200" aria-hidden="true">
    <polygon points="896,0 960,0 960,1200 66,1200" fill="var(--stage-copper)"/>
  </svg>

  <section class="card card-front" aria-label="Card front">
    <svg class="card-shapes" viewBox="0 0 1029 572" preserveAspectRatio="none" aria-hidden="true">
      <polygon points="824,0 1029,0 1029,572 739,572 386,448" fill="var(--card-brown)"/>
      <polygon points="386,448 744,6 770,150" fill="var(--sliver-green)" opacity="0.8"/>
      <polygon points="386,448 770,150 700,260" fill="var(--sliver-brown)" opacity="0.5"/>
    </svg>
    <div class="portrait" role="img" aria-label="Portrait photo of Mateo Ferrer"></div>
    <h1 class="person-name">Mateo Ferrer</h1>
    <p class="person-role">Founder &amp; Growth Hacker</p>
    <div class="contact-pill pill-email">
      <svg width="24" height="16" viewBox="0 0 24 16" aria-hidden="true">
        <rect x="1" y="1" width="22" height="14" fill="none" stroke="#fff" stroke-width="2"/>
        <polyline points="1,1 12,9 23,1" fill="none" stroke="#fff" stroke-width="2"/>
      </svg>
      <span>mf@copperridgehub.example</span>
    </div>
    <div class="contact-pill pill-phone">
      <svg width="28" height="28" viewBox="0 0 28 28" aria-hidden="true">
        <circle cx="14" cy="14" r="14" fill="#fff"/>
        <path d="M9 7.5c1-.8 2-.6 2.5.3l1.4 2.6c.4.8.1 1.5-.6 2l-.8.6c.7 1.8 2 3.2 3.7 4l.7-.8c.6-.7 1.3-.9 2-.5l2.5 1.5c.9.5 1 1.6.2 2.5-1.3 1.4-3 1.6-4.8.8-3.6-1.6-6.3-4.5-7.6-8-.6-1.9-.1-3.6 1-4.5z" fill="var(--card-green)"/>
      </svg>
      <span>+34 600 555 123</span>
    </div>
    <div class="brand-tile" aria-hidden="true"></div>
    <p class="brand-name">COPPER RIDGE</p>
  </section>

  <section class="card card-back" aria-label="Card back">
    <svg class="card-shapes" viewBox="0 0 1029 572" preserveAspectRatio="none" aria-hidden="true">
      <defs>
        <linearGradient id="back-fade" x1="0" y1="0" x2="1" y2="1">
          <stop offset="0.45" stop-color="#674f22"/>
          <stop offset="1" stop-color="#676a2e"/>
        </linearGradient>
      </defs>
      <rect x="0" y="402" width="1029" height="170" fill="url(#back-fade)"/>
      <polygon points="0,200 669,283 724,267 1029,167 584,402 0,402" fill="var(--card-green)"/>
      <polygon points="0,200 560,402 430,402" fill="var(--card-brown)" opacity="0.55"/>
      <polygon points="669,283 724,267 584,402" fill="var(--sliver-brown)" opacity="0.3"/>
    </svg>
    <div class="brand-tile" aria-hidden="true"></div>
    <p class="brand-name">COPPER RIDGE</p>
    <div class="contact-pill pill-web">
      <svg width="24" height="24" viewBox="0 0 24 24" aria-hidden="true" fill="none" stroke="#fff" stroke-width="1.5">
        <circle cx="12" cy="12" r="10.5"/>
        <ellipse cx="12" cy="12" rx="4.5" ry="10.5"/>
        <line x1="12" y1="1.5" x2="12" y2="22.5"/>
        <line x1="1.5" y1="12" x2="22.5" y2="12"/>
        <line x1="3.5" y1="6.5" x2="20.5" y2="6.5"/>
        <line x1="3.5" y1="17.5" x2="20.5" y2="17.5"/>
      </svg>
      <span>copperridgehub.example</span>
    </div>
  </section>
</main>
</body>
</html>
```